Design a WordPress layout for a home loans company

The home loans company in question is going through a rebrand and needs a new website layout.
Sites they like: http://www.brightnestlending.com.au/
Current logo: Attached.
Colours to be used: As per those used in logo.
Primary: #71aa3d
Secondary: #130e10
Pages to be designed:
- Homepage
- Internal services page
Menu items for display purposes:
- Home
- About Us
- Speak to a Broker
- Articles
- Contact Us
A modern design with simplicity is key.
For copy, dummy text such as Lorem ipsum will be fine.
If you would like anything elso, please ask.
Target Market(s)
25-40 year old
Mostly female
Buying their first home in most cases
Industry/Entity Type
Mortgage Brokerage
Number of Pages Required
2 page
Colors
Designer to choose colors to be used in the design.
Look and feel

```html
<!DOCTYPE html>
<html lang="en">
<head>
<meta charset="utf-8">
<title>Tallowbrook Loans – Home</title>
<link href="https://fonts.googleapis.com/css2?family=Raleway:wght@400;500;600;700;800&display=swap" rel="stylesheet">
<style>
:root{
  --green:#71aa3d;
  --green-dark:#5d9130;
  --ink:#130e10;
  --text:#444;
  --muted:#777;
  --white:#fff;
  --dark-panel:#1d1a1a;
}
*{box-sizing:border-box;margin:0;padding:0}
html,body{width:1200px;height:3390px;overflow:hidden}
body{position:relative;font-family:"Raleway",Arial,sans-serif;color:var(--text);background:var(--white)}
.abs{position:absolute}
a{color:inherit;text-decoration:none}
.btn{display:inline-block;background:var(--green);color:var(--white);font-weight:600;font-size:11px;padding:8px 22px;border-radius:2px}
.btn-outline{display:inline-block;border:2px solid var(--white);color:var(--white);font-weight:600;font-size:12px;padding:6px 20px;text-align:center}
.photo{position:absolute}

/* header */
.topbar{top:0;left:0;width:1200px;height:22px;font-size:10px;color:var(--muted)}
.topbar .social{left:345px;top:4px;display:flex;gap:12px}
.topbar .social span{width:9px;height:9px;border-radius:50%;background:var(--green);display:block}
.topbar .contact{right:150px;top:4px;display:flex;gap:18px;align-items:center}
.topbar .contact i{display:inline-block;width:12px;height:8px;background:var(--green);margin-right:5px;vertical-align:middle}
.logo{left:158px;top:14px;width:148px;height:58px;border:2px solid var(--green);display:flex;align-items:center;justify-content:center;flex-direction:column;background:var(--white)}
.logo b{font-size:20px;font-weight:800;color:var(--green);line-height:1}
.logo small{font-size:9px;font-weight:700;color:var(--green);letter-spacing:3px;margin-top:4px}
.nav{left:480px;top:42px;display:flex;gap:32px;font-size:12px;font-weight:600;color:var(--ink)}
.nav .active{border-bottom:3px solid var(--green);padding-bottom:8px}
.header-ctas{right:155px;top:36px;display:flex;gap:10px}
.header-ctas .btn{padding:7px 14px}

/* hero */
.hero{top:75px;left:0;width:1200px;height:450px;background:linear-gradient(100deg,#4a5a3a 0%,#8a7a66 40%,#c8bfb2 70%,#6f6458 100%)}
.hero-box{left:334px;top:237px;width:534px;height:120px;background:rgba(113,170,61,.92);color:var(--white);text-align:center;padding-top:18px}
.hero-box h1{font-size:29px;font-weight:700;display:flex;align-items:center;justify-content:center;gap:14px}
.hero-box h1::before,.hero-box h1::after{content:"";width:40px;height:2px;background:var(--white)}
.hero-box p{font-size:13px;font-weight:600;line-height:2;margin-top:8px}

/* divider */
.divider{width:20px;left:590px}
.divider .dash{width:0;margin:0 auto;border-left:2px dashed var(--ink)}
.divider svg{display:block;margin:2px auto 0}

.section-title{width:1200px;left:0;text-align:center;font-size:31px;font-weight:700;color:var(--ink);display:flex;justify-content:center;align-items:center;gap:8px}
.section-title::before,.section-title::after{content:"";width:38px;height:2px;background:var(--ink)}

.about-text{left:200px;top:673px;width:800px;text-align:center;font-size:10px;line-height:2.2;color:var(--muted)}
.about-btn{left:546px;top:779px}
.green-band{left:0;top:1035px;width:1200px;height:65px;background:var(--green)}
.about-photo{left:147px;top:841px;width:902px;height:257px;background:linear-gradient(180deg,#bcd3e6 0%,#c9d3d6 35%,#8b8c86 60%,#6f8a4e 85%,#5a7a3a 100%)}

/* broker */
.broker{left:149px;top:1236px;width:902px;height:460px;background:var(--white);box-shadow:0 2px 14px rgba(0,0,0,.15)}
.broker-green{left:0;top:0;width:450px;height:460px;background:var(--green)}
.broker-photo{left:77px;top:75px;width:377px;height:307px;background:linear-gradient(135deg,#d9d2c6,#a79682 55%,#5f564c)}
.broker-copy{left:482px;top:40px;width:390px}
.broker-copy h2{font-size:29px;font-weight:700;color:var(--ink);display:flex;align-items:center;gap:10px}
.broker-copy h2::after{content:"";width:38px;height:2px;background:var(--ink)}
.broker-copy p{font-size:10px;line-height:2.05;color:var(--muted);margin-top:18px}
.broker-copy .btn{margin-top:18px}

/* steps */
.step{width:140px;text-align:center}
.step .circle{width:86px;height:86px;border:2px solid var(--ink);border-radius:50%;margin:0 auto;display:flex;align-items:center;justify-content:center;background:var(--white)}
.step .label{background:var(--green);color:var(--white);font-size:11px;font-weight:600;padding:5px 0;margin-top:-6px;position:relative}
.arrow{top:1788px}

/* cta */
.cta{left:0;top:1894px;width:1200px;height:84px;background:var(--green)}
.cta p{position:absolute;left:150px;top:32px;color:var(--white);font-size:16px;font-weight:700}
.cta p em{font-style:normal;color:var(--ink)}
.cta .btn-outline{position:absolute;left:912px;top:26px}

/* news */
.card{top:2165px;width:287px;height:390px;background:var(--white);box-shadow:0 1px 8px rgba(0,0,0,.15)}
.card .top{height:200px;background:var(--green);position:relative}
.card .thumb{left:20px;top:27px;width:247px;height:173px}
.card .date{left:121px;top:178px;width:44px;height:44px;border-radius:50%;background:var(--green);border:3px solid var(--white);color:var(--white);font-size:8px;font-weight:700;text-align:center;padding-top:8px;line-height:1.3}
.card .body{padding:30px 18px 0;font-size:10px;line-height:2;color:var(--muted)}
.card .more{color:var(--green);font-size:8px}
.card h3{position:absolute;left:18px;bottom:12px;right:18px;border-top:1px solid #ddd;padding-top:12px;font-size:17px;font-weight:500;color:var(--ink)}

/* contact */
.footer-bg{left:0;top:3040px;width:1200px;height:350px;background:var(--green)}
.query{left:149px;top:2756px;width:902px;height:373px;background:var(--dark-panel);border-top:3px solid var(--green)}
.query h2{position:absolute;left:38px;top:28px;color:var(--white);font-size:20px;font-weight:600}
.query h2 em{font-style:normal;color:var(--green)}
.field{position:absolute;height:34px;background:#3a3737;color:#ccc;font-size:9px;padding:10px 8px}
.query .submit{position:absolute;left:38px;top:310px;width:826px;height:30px;background:var(--green);color:var(--white);font-size:11px;font-weight:600;text-align:center;padding-top:8px}

/* footer */
.fcol{top:3170px;color:var(--white);font-size:10px;line-height:2.3}
.fcol h4{font-size:10px;font-weight:700;margin-bottom:8px}
.fcol .row{display:flex;gap:8px;align-items:flex-start;line-height:1.6;margin-bottom:10px}
.fcol .ic{width:11px;height:11px;background:var(--white);border-radius:2px;flex:none;margin-top:2px}
.prop{display:flex;gap:10px;margin-bottom:12px}
.prop .pic{width:48px;height:42px;flex:none;background:linear-gradient(135deg,#b8c2b0,#6b7a5c)}
.prop span{line-height:1.5}
.prop b{display:block;font-weight:600}
.flogo{left:912px;top:3175px;width:140px;text-align:center}
.flogo .logo{position:static;width:140px;height:56px;border-color:var(--white);background:transparent}
.flogo .logo b,.flogo .logo small{color:var(--white)}
.fsocial{display:flex;justify-content:center;gap:22px;margin:18px 0}
.fsocial span{width:10px;height:10px;border-radius:50%;background:var(--white)}
.copy{top:3370px;font-size:8px;color:var(--white)}
</style>
</head>
<body>

<div class="abs topbar">
  <div class="abs social"><span></span><span></span><span></span><span></span></div>
  <div class="abs contact"><span><i></i>info@tallowbrookloans.com</span><span><i></i>1300 482 615</span></div>
</div>
<div class="abs logo"><b>Tallowbrook</b><small>LOANS</small></div>
<nav class="abs nav"><a class="active">Home</a><a>About us</a><a>Services</a><a>Articles</a></nav>
<div class="abs header-ctas"><a class="btn">Contact Us</a><a class="btn">Find a broker</a></div>

<div class="abs hero photo" role="img" aria-label="Child running through the hallway of a new home with moving boxes"></div>
<div class="abs hero-box">
  <h1>GET YOUR FIRST HOME LOAN</h1>
  <p>We are a mortgage brokerage company providing best residential<br>and commercial mortgage services for our clients in Australia.</p>
</div>

<div class="abs divider" style="top:532px"><div class="dash" style="height:30px"></div><svg width="14" height="14" viewBox="0 0 14 14"><path d="M7 1 13 7H11V13H3V7H1Z" fill="var(--green)"/></svg></div>

<h2 class="abs section-title" style="top:610px">About Us</h2>
<p class="abs about-text">Lorem ipsum dolor sit amet, consectetur adipiscing elit. Donec vehicula eros urna, at tincidunt metus sollicitudin quis. Integer tincidunt leo at dui. Donec facilisis sem orci, non semper ut pellentesque ante egestas. Pellentesque accumsan mollis dapibus, congue enim ipsum dapibus nulla, quis egestas tellus lorem ac eros. Nullam sed tincidunt magna. Cras venenatis lacus at libero volutpat, ut sollicitudin sapien elementum. Cras blandit tortor sit amet felis porttitor, in placerat mauris lacinia. Curabitur at erat vitae mi aliquam rutrum sit amet eu turpis. Fusce enim nisl, aliquet id sem ut, tristique egestas nisi. Praesent ullamcorper tristique felis in placerat.</p>
<a class="abs btn about-btn">Learn More</a>

<div class="abs green-band"></div>
<div class="abs about-photo photo" role="img" aria-label="Large suburban house with a slate roof and front garden"></div>

<div class="abs divider" style="top:1117px"><div class="dash" style="height:90px"></div></div>

<section class="abs broker">
  <div class="abs broker-green"></div>
  <div class="abs broker-photo photo" role="img" aria-label="Couple meeting a mortgage broker at a living room table"></div>
  <div class="abs broker-copy">
    <h2>SPEAK TO A BROKER</h2>
    <p>Sed tempor lacus vel dui ornare maximus. Nulla pellentesque lobortis tempus. Quisque mauris arcu, efficitur a mattis sit amet, volutpat at metus. Nam et arcu a lectus gravida vehicula. Pellentesque varius nisl dui, vitae pellentesque nulla mattis et. Aenean quam lectus, facilisis non venenatis id, efficitur vel sapien. Mauris at felam. Donec eget lectus eget urna ornare gravida. Donec eget elementum ex, auctor vehicula arcu.</p>
    <p style="margin-top:12px">Praesent dapibus, nisl eget blandit ullamcorper, magna urna eleifend lacus, nec vehicula magna eros vel ligula. Vivamus sed sem vitae neque condimentum tempor vitae pellentesque nulla mattis et. Aenean quam lectus, facilisis non venenatis id, efficitur vel sapien. Mauris ut tellus non ipsum eleifend aliquam. Donec eget lectus eget urna ornare gravida. Donec eget elementum ex, auctor vehicula arcu.</p>
    <a class="btn">Find a broker</a>
  </div>
</section>

<div class="abs step" style="left:240px;top:1740px"><div class="circle"><svg width="44" height="44" viewBox="0 0 44 44" fill="none" stroke="var(--ink)" stroke-width="2"><rect x="6" y="8" width="32" height="22"/><circle cx="22" cy="17" r="4"/><path d="M15 28c2-5 12-5 14 0M10 38h24"/></svg></div><div class="label">Meet the broker</div></div>
<svg class="abs arrow" style="left:420px" width="60" height="12" viewBox="0 0 60 12"><path d="M0 6H56M50 1 57 6 50 11" stroke="var(--green)" stroke-width="2" fill="none"/></svg>
<div class="abs step" style="left:530px;top:1740px"><div class="circle"><svg width="44" height="44" viewBox="0 0 44 44" fill="none" stroke="var(--ink)" stroke-width="2"><path d="M8 22h6v16H8zM14 24l8-12c3 0 4 2 3 6h10c2 0 3 2 2 4l-3 12c-1 2-2 3-4 3H14"/></svg></div><div class="label">Get best advice</div></div>
<svg class="abs arrow" style="left:710px" width="60" height="12" viewBox="0 0 60 12"><path d="M0 6H56M50 1 57 6 50 11" stroke="var(--green)" stroke-width="2" fill="none"/></svg>
<div class="abs step" style="left:816px;top:1740px"><div class="circle"><svg width="44" height="44" viewBox="0 0 44 44" fill="none" stroke="var(--ink)" stroke-width="2"><rect x="6" y="18" width="22" height="14"/><circle cx="17" cy="25" r="3"/><path d="M28 20h8l4 6M30 12l6 4"/></svg></div><div class="label">Make Investment</div></div>

<section class="abs cta">
  <p>WANT TO BUY <em>HOME</em> OR MAKE AN <em>INVESTMENT</em>?</p>
  <a class="btn-outline">Find a Broker</a>
</section>

<div class="abs divider" style="top:1990px"><div class="dash" style="height:28px"></div><svg width="14" height="14" viewBox="0 0 14 14"><path d="M7 1 13 7H11V13H3V7H1Z" fill="var(--green)"/></svg></div>

<h2 class="abs section-title" style="top:2068px;font-size:28px;font-weight:600">News and Articles</h2>

<article class="abs card" style="left:149px"><div class="top"><div class="abs thumb photo" style="background:linear-gradient(135deg,#e8d6c0,#b88a62)" role="img" aria-label="Family gathered around a table at home"></div><div class="abs date">14<br>May</div></div><div class="body">Lorem ipsum dolor sit amet, consectetur adipiscing elit. Aenean egestas enim eu lectus imperdiet scelerisque. Pellentesque habitant morbi tristique senectus et netus ........<br><span class="more">Read more</span></div><h3>Buy your first home</h3></article>
<article class="abs card" style="left:456px"><div class="top"><div class="abs thumb photo" style="background:linear-gradient(135deg,#f4f4f2,#c9c6bf)" role="img" aria-label="Couple holding a card with a house sketch"></div><div class="abs date">08<br>Dec</div></div><div class="body">Lorem ipsum dolor sit amet, consectetur adipiscing elit. Aenean egestas enim eu lectus imperdiet scelerisque. Pellentesque habitant morbi tristique senectus et netus ........<br><span class="more">Read more</span></div><h3>Buy your next home</h3></article>
<article class="abs card" style="left:763px"><div class="top"><div class="abs thumb photo" style="background:linear-gradient(135deg,#a6c878,#6f8a3e 50%,#c79a5c)" role="img" aria-label="Wooden house models beside stacks of coins"></div><div class="abs date">22<br>May</div></div><div class="body">Lorem ipsum dolor sit amet, consectetur adipiscing elit. Aenean egestas enim eu lectus imperdiet scelerisque. Pellentesque habitant morbi tristique senectus et netus ........<br><span class="more">Read more</span></div><h3>Buy an investment property</h3></article>

<a class="abs btn" style="left:550px;top:2588px">See more</a>
<div class="abs divider" style="top:2642px"><div class="dash" style="height:32px"></div><svg width="14" height="14" viewBox="0 0 14 14"><path d="M7 1 13 7H11V13H3V7H1Z" fill="var(--green)"/></svg></div>

<div class="abs footer-bg"></div>
<section class="abs query">
  <h2>Have any query? <em>Contact</em> our expert!</h2>
  <div class="field" style="left:38px;top:84px;width:262px">First Name</div>
  <div class="field" style="left:318px;top:84px;width:262px">Last Name</div>
  <div class="field" style="left:598px;top:84px;width:266px">Email</div>
  <div class="field" style="left:38px;top:138px;width:262px">Phone Number</div>
  <div class="field" style="left:318px;top:138px;width:262px">State</div>
  <div class="field" style="left:598px;top:138px;width:266px">Postcode</div>
  <div class="field" style="left:38px;top:192px;width:826px;height:100px">Your Inquiry here...</div>
  <div class="submit">Contact Us</div>
</section>

<div class="abs fcol" style="left:149px"><h4>QUICK LINKS</h4>Home<br>About Us<br>Services<br>Articles<br>Contact Us</div>
<div class="abs fcol" style="left:350px;width:170px"><h4>CONTACT INFO</h4>
  <div class="row"><span class="ic"></span>info@tallowbrookloans.com</div>
  <div class="row"><span class="ic"></span>1300 482 615</div>
  <div class="row"><span class="ic" style="border-radius:50%"></span>Lorem ipsum dolor sit amet, consectetur adipiscing elit.</div>
</div>
<div class="abs fcol" style="left:617px;width:180px"><h4>RECENT PROPERTIES</h4>
  <div class="prop"><div class="pic" role="img" aria-label="Property thumbnail"></div><span>Lorem ipsum dolor sit amet, consectetur<b>$21,000</b></span></div>
  <div class="prop"><div class="pic" role="img" aria-label="Property thumbnail"></div><span>Lorem ipsum dolor sit amet, consectetur<b>$28,000</b></span></div>
</div>
<div class="abs flogo">
  <div class="logo"><b>Tallowbrook</b><small>LOANS</small></div>
  <div class="fsocial"><span></span><span></span><span></span><span></span></div>
  <a class="btn-outline" style="width:140px">Contact Us</a>
</div>
<p class="abs copy" style="left:149px">©2024 Tallowbrook Loans. All Rights Reserved</p>
<p class="abs copy" style="left:928px">Terms of use | Privacy Policy</p>

</body>
</html>
```